Design a circle using words of various fonts

Simple project (WILL SELECT TODAY). Need Artwork that is comprised of words (single and short phrases - provided) that when arranged form the shape of a circle.

The words and phrases that are attached currently form a rectangle. Not all words and phrases are needed - you have creative freedom.

Would like a variety of fonts to be used. All art is to be 1 color.

This is going to be used as a gift. We will laser engrave the final design onto a circular piece of wood that is 18" in diameter...so we don't need all the words and phrases. Just something that looks good hanging on a wall and can be read from 5 feet or more away.

More than enough words in the attached 3 images to draw from. Remember, not about quantity of words, just need good looking .

Like to have final file in vector format (text converted to curves)

Will decide today (July 16th)

```html
<!DOCTYPE html>
<html lang="en">
<head>
<meta charset="utf-8">
<title>Lake Words Circle</title>
<link rel="stylesheet" href="https://fonts.googleapis.com/css2?family=Alegreya+SC:wght@500;700&family=Kanit:wght@600&family=Federant&family=Zilla+Slab:wght@700&family=Baumans&display=swap">
<style>
  :root {
    --paper: #ffffff;
    --ring-line: #1a1a1a;
    --ring-shadow: #9a9a9a;
    --outer-ink: #e8336b;
    --inner-ink: #3c9a1f;
  }
  html, body {
    margin: 0;
    padding: 0;
    width: 1200px;
    height: 749px;
    overflow: hidden;
    background: var(--paper);
  }
  .word-circle {
    display: block;
    width: 1200px;
    height: 749px;
  }
  .ring-line { fill: none; stroke: var(--ring-line); stroke-width: 2; }
  .ring-shadow { fill: none; stroke: var(--ring-shadow); stroke-width: 3; opacity: .55; }
  .outer-words { fill: var(--outer-ink); }
  .inner-words { fill: var(--inner-ink); }
  .phrase-relax  { font-family: "Alegreya SC", serif; font-weight: 700; }
  .phrase-grateful { font-family: "Alegreya SC", serif; font-weight: 500; }
  .phrase-campfire { font-family: "Kanit", sans-serif; font-weight: 600; }
  .phrase-seaside { font-family: "Federant", serif; }
  .phrase-cookout { font-family: "Zilla Slab", serif; font-weight: 700; }
  .phrase-cruises { font-family: "Baumans", sans-serif; }
  .phrase-lake { font-family: "Alegreya SC", serif; font-weight: 700; }
  .outer-words text { font-size: 27px; }
  .outer-words .phrase-cookout { font-size: 33px; }
  .inner-words text { font-size: 20px; }
  .inner-words .phrase-cookout { font-size: 25px; }
</style>
</head>
<body>
<svg class="word-circle" viewBox="0 0 1200 749" xmlns="http://www.w3.org/2000/svg">
  <defs>
    <filter id="soft-shadow" x="-20%" y="-20%" width="140%" height="140%">
      <feGaussianBlur stdDeviation="3"/>
    </filter>
    <path id="outer-track" d="M579 704 A327 327 0 1 1 579 50 A327 327 0 1 1 579 704"/>
    <path id="inner-track" d="M579 620 A243 243 0 1 1 579 134 A243 243 0 1 1 579 620"/>
  </defs>

  <g class="rings">
    <circle class="ring-shadow" cx="582" cy="380" r="303" filter="url(#soft-shadow)"/>
    <circle class="ring-line" cx="579" cy="377" r="303"/>
    <circle class="ring-shadow" cx="582" cy="381" r="236" filter="url(#soft-shadow)"/>
    <circle class="ring-line" cx="579" cy="377" r="237" stroke-width="1.4"/>
  </g>

  <g class="outer-words">
    <text class="phrase-relax"><textPath href="#outer-track" startOffset="3.5%" textLength="300">• Sit back &amp; Relax</textPath></text>
    <text class="phrase-grateful"><textPath href="#outer-track" startOffset="20.5%" textLength="165">• Be grateful</textPath></text>
    <text class="phrase-campfire"><textPath href="#outer-track" startOffset="30.5%" textLength="320">• Build a campfire</textPath></text>
    <text class="phrase-seaside"><textPath href="#outer-track" startOffset="47.5%" textLength="250">• Seaside Report</textPath></text>
    <text class="phrase-cookout"><textPath href="#outer-track" startOffset="60.2%" textLength="315">• Cookout Enjoy</textPath></text>
    <text class="phrase-cruises"><textPath href="#outer-track" startOffset="76%" textLength="255">• booze cruises</textPath></text>
    <text class="phrase-lake"><textPath href="#outer-track" startOffset="89%" textLength="205">• Lake Rules</textPath></text>
  </g>

  <g class="inner-words">
    <text class="phrase-relax"><textPath href="#inner-track" startOffset="4%" textLength="215">• Sit back &amp; Relax</textPath></text>
    <text class="phrase-grateful"><textPath href="#inner-track" startOffset="20%" textLength="120">• Be grateful</textPath></text>
    <text class="phrase-campfire"><textPath href="#inner-track" startOffset="29.5%" textLength="230">• Build a campfire</textPath></text>
    <text class="phrase-seaside"><textPath href="#inner-track" startOffset="45.5%" textLength="200">• Seaside Report</textPath></text>
    <text class="phrase-cookout"><textPath href="#inner-track" startOffset="58.8%" textLength="245">• Cookout Enjoy</textPath></text>
    <text class="phrase-cruises"><textPath href="#inner-track" startOffset="75.3%" textLength="200">• booze cruises</textPath></text>
    <text class="phrase-lake"><textPath href="#inner-track" startOffset="89%" textLength="150">• Lake Rules</textPath></text>
  </g>
</svg>
</body>
</html>
```